KF ELECTRICAL SERVICES

I am just setting up on my own as an electrician. I want a 2 sided business card that is eye catching on the front and has skills on the back. I do domestic, commercial and agricultural work.
Inspection and Testing.
Rewires.
Fuseboards.
New builds.
Fault finding.
Free quotations
All work undertaken.
10 years experience.
Registered and insured by LUSCOR.
Customer references available on request.
Kevin Farrow. Mob. 07915268430. Home 01563470958.
Email. mertowe.kf@postlark.com.
My own unique logo would be nice either electrical related or KF initial related.
After seeing all the designs I prefer something simple but striking. My favourite so far is just black background blue and red writing and is simple but striking. And a KF with something electrical incorporated into it.

Electrical

• Services and a good logo or graphic.

```html
<!DOCTYPE html>
<html lang="en">
<head>
<meta charset="utf-8">
<title>KF Electrical Services – Business Card</title>
<link rel="stylesheet" href="https://fonts.googleapis.com/css2?family=Michroma&display=swap">
<style>
  :root {
    --page: #e9e9e9;
    --charcoal: #232323;
    --charcoal-soft: #3a3a3a;
    --lime: #c8e600;
    --green-deep: #2f4f12;
    --green-mid: #5d8a22;
    --green-text: #7cbf2a;
    --ink: #2b2b2b;
    --grey: #555555;
    --white: #ffffff;
    --badge-red: #d9382c;
    --badge-blue: #2f5aa8;
  }
  * { box-sizing: border-box; margin: 0; padding: 0; }
  html, body {
    width: 1200px; height: 873px; overflow: hidden;
    background: var(--page);
    font-family: "Michroma", sans-serif;
  }
  .card {
    position: absolute; top: 270px;
    width: 520px; height: 330px;
    overflow: hidden;
    box-shadow: 0 8px 24px rgba(0,0,0,.18);
  }

  /* ---------- Back side ---------- */
  .card-back { left: 60px; background: var(--white); }
  .back-header {
    position: absolute; left: 0; top: 0; width: 100%; height: 68px;
    background: linear-gradient(90deg, var(--charcoal) 0%, var(--charcoal-soft) 70%, #9a9a9a 100%);
    display: flex; align-items: center; justify-content: center;
  }
  .back-title { color: var(--lime); font-size: 20px; letter-spacing: 1px; }
  .sector-band {
    position: absolute; left: 0; top: 68px; width: 100%; height: 40px;
    background: var(--lime);
    display: flex; align-items: center; justify-content: center;
    color: var(--ink); font-size: 11.5px; letter-spacing: .3px;
  }
  .services-list {
    position: absolute; left: 0; top: 126px; width: 100%;
    text-align: center; color: var(--ink);
    font-size: 11.5px; line-height: 19px;
  }
  .highlight {
    position: absolute; left: 0; top: 178px; width: 100%;
    text-align: center; color: var(--green-text); font-size: 12.5px;
  }
  .highlight .divider { color: var(--grey); }
  .references {
    position: absolute; left: 0; top: 202px; width: 100%;
    text-align: center; color: var(--grey); font-size: 10.5px;
  }
  .badges {
    position: absolute; left: 0; top: 238px; width: 100%;
    display: flex; justify-content: center; gap: 54px;
  }
  .badge { width: 58px; height: 50px; }
  .badge-trust { background: var(--badge-red); border-radius: 4px; }
  .badge-scheme { background: var(--badge-blue); border-radius: 50%; width: 50px; }

  /* ---------- Front side ---------- */
  .card-front { left: 620px; background: var(--charcoal); }
  .storm-area {
    position: absolute; left: 0; top: 170px; width: 100%; height: 160px;
    background: radial-gradient(ellipse at 70% 45%, var(--green-mid) 0%, var(--green-deep) 60%, #1d2e0b 100%);
  }
  .swoosh { position: absolute; left: 0; top: 140px; width: 520px; height: 70px; }
  .brand {
    position: absolute; right: 34px; top: 18px; text-align: right;
  }
  .brand-mark { color: var(--lime); font-size: 66px; line-height: 1; letter-spacing: 2px; }
  .brand-sub { color: var(--white); font-size: 11px; letter-spacing: 2px; margin-top: 6px; }
  .name-band {
    position: absolute; left: 0; top: 22px; width: 230px; height: 30px;
    background: var(--lime);
    clip-path: polygon(0 0, 100% 0, 88% 100%, 0 100%);
    display: flex; align-items: center; padding-left: 20px;
    color: var(--ink); font-size: 12px; letter-spacing: 1px;
  }
  .phones {
    position: absolute; left: 20px; top: 70px;
    color: var(--white); font-size: 10.5px; line-height: 20px;
  }
  .label { color: var(--lime); margin-right: 6px; }
  .web-details {
    position: absolute; left: 40px; top: 238px;
    color: var(--white); font-size: 10.5px; line-height: 24px;
  }
</style>
</head>
<body>

<section class="card card-back" aria-label="Business card back">
  <div class="back-header"><h2 class="back-title">SERVICES</h2></div>
  <div class="sector-band">DOMESTIC, COMMERCIAL &amp; AGRICULTURAL WORK.</div>
  <p class="services-list">INSPECTION &amp; TESTING, REWIRES, FUSEBOARDS,<br>NEW BUILDS AND FAULT FINDING</p>
  <p class="highlight">ALL WORK UNDERTAKEN <span class="divider">|</span> 10 YEARS EXPERIENCE</p>
  <p class="references">CUSTOMER REFERENCES AVAILABLE ON REQUEST</p>
  <div class="badges">
    <div class="badge badge-trust" role="img" aria-label="Trade standards badge"></div>
    <div class="badge badge-scheme" role="img" aria-label="LUSCOR registration badge"></div>
  </div>
</section>

<section class="card card-front" aria-label="Business card front">
  <div class="storm-area" role="img" aria-label="Green lightning storm graphic"></div>
  <svg class="swoosh" viewBox="0 0 520 70" aria-hidden="true">
    <path d="M0 30 C 180 62, 380 60, 520 10 L520 0 C 380 48, 180 50, 0 22 Z" fill="var(--white)"/>
    <path d="M0 30 C 180 62, 380 60, 520 10 L520 70 L0 70 Z" fill="transparent"/>
  </svg>
  <div class="brand">
    <div class="brand-mark">K&amp;F</div>
    <div class="brand-sub">ELECTRICAL SERVICES</div>
  </div>
  <div class="name-band">KEVIN FARROW</div>
  <div class="phones">
    <p><span class="label">M</span>07915 268 430</p>
    <p><span class="label">H</span>01563 470 958</p>
  </div>
  <div class="web-details">
    <p><span class="label">E</span>MERTOWE.KF@POSTLARK.COM</p>
    <p><span class="label">W</span>WWW.KFSPARKWORKS.NET</p>
  </div>
</section>

</body>
</html>
```